Webdesign für Gravierwerkstatt
Zielgruppe
Das Unternehmen ist eine Gravierwerkstatt - die Zielgruppe sind sowohl private als auch gewerbliche Kunden und Vereine für Einzelauftrgäge oder Kleinserien für Gravuren
Aufgabenstellung
- modernes Layout
- Farbgebung blau, hellblau, Grau, weiß
- übersichtliche Darstellung der angebotenen Leistungen
- kein Kontaktformular
- nicht zu viele Bilder
- es existiert kein richtiges Logo, (es kann aber das Handwerkszeichen wiederverwendet werden)
- Names des Unternehmens 'Gravierwerkstatt Brenner'
- Meisterwerkstatt

```html
<!DOCTYPE html>
<html lang="de">
<head>
<meta charset="utf-8">
<title>Gravierwerkstatt Brenner – Meisterbetrieb</title>
<link href="https://fonts.googleapis.com/css2?family=Inter:wght@400;500;600;700&display=swap" rel="stylesheet">
<style>
:root{
  --blue:#2563eb;
  --blue-soft:#eef4ff;
  --ink:#0f172a;
  --text:#475569;
  --muted:#64748b;
  --line:#e2e8f0;
  --panel:#f7f9fc;
  --white:#ffffff;
  --hero-tone-a:#8e9aa0;
  --hero-tone-b:#7a6452;
  --wood-tone-a:#6e5442;
  --wood-tone-b:#a87c58;
}
*{box-sizing:border-box;margin:0;padding:0}
html,body{width:1200px;height:2643px;overflow:hidden}
body{font-family:"Inter",sans-serif;color:var(--ink);background:var(--white);position:relative}
.abs{position:absolute}
svg.ic{width:20px;height:20px;fill:none;stroke:var(--blue);stroke-width:1.8;stroke-linecap:round;stroke-linejoin:round}

/* hero */
.hero{position:absolute;left:0;top:0;width:1200px;height:793px;overflow:hidden;background:#f3f4f6}
.hero-photo{position:absolute;inset:0;background:linear-gradient(180deg,var(--hero-tone-a) 0%,var(--hero-tone-b) 100%)}
.hero-fade{position:absolute;inset:0;background:linear-gradient(90deg,rgba(246,247,249,1) 0%,rgba(246,247,249,.96) 38%,rgba(246,247,249,.55) 58%,rgba(246,247,249,0) 80%)}
.nav{position:absolute;left:67px;top:20px;width:1066px;height:68px;background:rgba(255,255,255,.96);border-radius:14px;box-shadow:0 4px 20px rgba(15,23,42,.06)}
.brand{position:absolute;left:22px;top:16px;display:flex;align-items:center;gap:10px}
.brand-mark{width:30px;height:30px;border-radius:50%;background:var(--ink)}
.brand-name{font-weight:600;font-size:16px;line-height:18px}
.brand-sub{font-size:10px;letter-spacing:2px;color:var(--muted);margin-top:2px}
.nav-links{position:absolute;left:420px;top:0;height:68px;display:flex;gap:34px;font-size:14px;color:#334155}
.nav-links a{line-height:68px;text-decoration:none;color:inherit;position:relative}
.nav-links a.active{color:var(--blue)}
.nav-links a.active::after{content:"";position:absolute;left:0;right:0;bottom:4px;height:2px;background:var(--blue);border-radius:2px}
.call{position:absolute;right:22px;top:18px;height:32px;padding:0 16px;border-radius:16px;background:var(--blue-soft);color:var(--blue);font-size:12.5px;display:flex;align-items:center;gap:6px}
.call svg{width:14px;height:14px}
.badge{left:67px;top:160px;height:31px;padding:0 14px;border-radius:16px;background:var(--blue-soft);border:1px solid #d7e3fb;color:#1d4ed8;font-size:12px;font-weight:600;display:flex;align-items:center;gap:8px;letter-spacing:.2px}
.badge svg{width:13px;height:13px}
h1{left:67px;top:218px;font-size:56px;line-height:57px;font-weight:700;letter-spacing:-1.2px}
h1 span{color:var(--blue)}
.lead{left:67px;top:407px;width:440px;font-size:17px;line-height:27px;color:#334155}
.btn{top:521px;height:46px;border-radius:8px;font-size:14px;font-weight:600;display:flex;align-items:center;justify-content:center;gap:10px}
.btn-dark{left:67px;width:183px;background:var(--ink);color:#fff}
.btn-dark svg{stroke:#fff;width:15px;height:15px}
.btn-light{left:264px;width:175px;background:#fff;border:1px solid var(--line)}
.stats-rule{left:67px;top:616px;width:480px;height:1px;background:rgba(15,23,42,.08)}
.stat{top:644px}
.stat b{display:block;font-size:21px;font-weight:600}
.stat small{display:block;font-size:12px;letter-spacing:1px;color:var(--muted);margin-top:3px}
.stat-sep{top:648px;width:1px;height:32px;background:rgba(15,23,42,.12)}

/* services */
.sec-title{font-size:31px;font-weight:600;letter-spacing:-.5px}
.services-head{left:87px;top:872px}
.services-lead{left:87px;top:920px;width:530px;font-size:15px;line-height:24px;color:var(--text)}
.dots{left:980px;top:963px;display:flex;gap:7px}
.dots i{width:40px;height:3px;border-radius:2px;background:#e2e8f0}
.dots i:first-child{background:var(--blue)}
.card{top:1020px;width:325px;height:275px;background:var(--panel);border:1px solid #eef1f5;border-radius:16px;padding:34px}
.card-icon{width:46px;height:46px;border-radius:10px;background:#fff;box-shadow:0 2px 8px rgba(15,23,42,.06);display:flex;align-items:center;justify-content:center}
.card h3{font-size:20px;font-weight:600;margin:30px 0 20px}
.card li{list-style:none;font-size:14px;color:#334155;line-height:20px;margin-bottom:13px;padding-left:15px;position:relative}
.card li::before{content:"";position:absolute;left:0;top:8px;width:5px;height:5px;border-radius:50%;background:var(--blue)}

/* about */
.about{left:0;top:1375px;width:1200px;height:538px;background:var(--panel)}
.about-title{left:67px;top:1484px}
.about-text{left:67px;top:1552px;width:490px;font-size:15px;line-height:24.5px;color:var(--text)}
.about-text p{margin-bottom:20px}
.about-text strong{color:var(--ink);font-weight:600}
.cert{left:67px;top:1752px;display:flex;align-items:center;gap:14px}
.cert-icon{width:53px;height:53px;border-radius:50%;background:#fff;border:1px solid var(--line);display:flex;align-items:center;justify-content:center}
.cert-icon svg{width:24px;height:24px}
.cert b{display:block;font-size:15px;font-weight:600}
.cert small{display:block;font-size:12px;letter-spacing:1.5px;color:var(--muted);margin-top:3px}
.about-photo{left:627px;top:1455px;width:506px;height:379px;border-radius:22px;box-shadow:0 18px 40px rgba(15,23,42,.18);
  background:linear-gradient(180deg,var(--wood-tone-a) 0%,var(--wood-tone-b) 100%)}

/* contact */
.contact{left:67px;top:1995px;width:1066px;height:495px;background:var(--panel);border:1px solid #eef1f5;border-radius:40px}
.contact-title{left:135px;top:2063px;line-height:34px}
.info{left:135px;display:flex;gap:21px;align-items:center}
.info-icon{width:45px;height:45px;border-radius:10px;background:#fff;box-shadow:0 2px 8px rgba(15,23,42,.06);display:flex;align-items:center;justify-content:center}
.info small{display:block;font-size:11.5px;letter-spacing:1.8px;color:var(--muted);margin-bottom:5px}
.info span{font-size:16px}
.hours{left:634px;top:2063px;width:431px;height:360px;background:#fff;border-radius:20px;box-shadow:0 6px 24px rgba(15,23,42,.05);padding:34px 33px}
.hours h3{font-size:20px;font-weight:600;margin-bottom:22px}
.row{display:flex;justify-content:space-between;font-size:14px;height:54px;align-items:center;border-bottom:1px solid #eef1f5;color:var(--text)}
.row:last-of-type{border-bottom:0}
.row b{color:var(--ink);font-weight:600}
.row em{font-style:normal;color:#94a3b8}
.note{margin-top:22px;background:var(--blue-soft);border-radius:12px;padding:18px 20px;display:flex;gap:14px;font-size:12px;line-height:19px;color:#1e40af}
.note svg{width:20px;height:20px;flex:none;margin-top:4px}

/* footer */
.footer-rule{left:0;top:2572px;width:1200px;height:1px;background:#eef1f5}
.footer-copy{left:87px;top:2598px;font-size:12px;color:var(--muted)}
.footer-links{right:87px;top:2598px;display:flex;gap:20px;font-size:12px;color:var(--muted)}
</style>
</head>
<body>

<header class="hero">
  <div class="hero-photo" role="img" aria-label="Foto: Lasergravurmaschine mit Funkenflug bei der Metallbearbeitung"></div>
  <div class="hero-fade"></div>
  <nav class="nav">
    <div class="brand">
      <div class="brand-mark"></div>
      <div><div class="brand-name">Gravierwerkstatt Brenner</div><div class="brand-sub">MEISTERBETRIEB</div></div>
    </div>
    <div class="nav-links"><a class="active">Startseite</a><a>Leistungen</a><a>Über uns</a><a>Kontakt</a></div>
    <div class="call"><svg class="ic" viewBox="0 0 24 24"><path d="M22 16.9v3a2 2 0 0 1-2.2 2 19.8 19.8 0 0 1-8.6-3.1 19.5 19.5 0 0 1-6-6A19.8 19.8 0 0 1 2.1 4.2 2 2 0 0 1 4.1 2h3a2 2 0 0 1 2 1.7c.1 1 .4 1.9.7 2.8a2 2 0 0 1-.5 2.1L8 9.9a16 16 0 0 0 6 6l1.3-1.3a2 2 0 0 1 2.1-.4c.9.3 1.8.6 2.8.7a2 2 0 0 1 1.7 2z"/></svg>Anrufen</div>
  </nav>
  <div class="abs badge"><svg class="ic" viewBox="0 0 24 24"><circle cx="12" cy="8" r="6"/><path d="M8.2 13.1 7 22l5-3 5 3-1.2-8.9"/></svg>PRÄZISION SEIT GENERATIONEN</div>
  <h1 class="abs">Meisterhafte<br>Gravuren<br><span>mit Leidenschaft</span></h1>
  <p class="abs lead">Wo traditionelles Handwerk auf modernste Lasertechnologie trifft. Wir veredeln Ihre Werkstücke mit höchster Präzision und handwerklicher Perfektion.</p>
  <div class="abs btn btn-dark">Projekt anfragen <svg class="ic" viewBox="0 0 24 24"><path d="M5 12h14M13 6l6 6-6 6"/></svg></div>
  <div class="abs btn btn-light">Unsere Leistungen</div>
  <div class="abs stats-rule"></div>
  <div class="abs stat" style="left:67px"><b>100%</b><small>PRÄZISION</small></div>
  <div class="abs stat-sep" style="left:161px"></div>
  <div class="abs stat" style="left:189px"><b>Meister</b><small>BETRIEB</small></div>
  <div class="abs stat-sep" style="left:288px"></div>
  <div class="abs stat" style="left:316px"><b>Handmade</b><small>IN GERMANY</small></div>
</header>

<h2 class="abs sec-title services-head">Handwerkliche Perfektion</h2>
<p class="abs services-lead">Von der klassischen Gravur bis zur modernen Lasertechnik – wir bieten maßgeschneiderte Lösungen für jedes Material.</p>
<div class="abs dots"><i></i><i></i><i></i></div>

<section class="abs card" style="left:87px">
  <div class="card-icon"><svg class="ic" viewBox="0 0 24 24"><path d="M13 2 3 14h9l-1 8 10-12h-9z"/></svg></div>
  <h3>Lasergravur</h3>
  <ul><li>Industrieschilder &amp; Skalen</li><li>Werbeartikel Veredelung</li><li>Präzise Serienfertigung</li></ul>
</section>
<section class="abs card" style="left:438px">
  <div class="card-icon"><svg class="ic" viewBox="0 0 24 24"><path d="m15 12-8.5 8.5a2.1 2.1 0 0 1-3-3L12 9"/><path d="M17.6 15 22 10.6M20.9 11.7l-1.3-1.3a2 2 0 0 1-.6-1.4v-.9L16.7 5.8A5.6 5.6 0 0 0 12.7 4H9.9l1 .9A6.2 6.2 0 0 1 13 9.3V11l2 2h1.2a2 2 0 0 1 1.4.6l1.2 1.3"/></svg></div>
  <h3>Handgravur</h3>
  <ul><li>Edle Trauring-Gravuren</li><li>Individuelle Monogramme</li><li>Unikate auf Edelmetall</li></ul>
</section>
<section class="abs card" style="left:789px">
  <div class="card-icon"><svg class="ic" viewBox="0 0 24 24"><path d="m12 2 10 5-10 5L2 7z"/><path d="m2 12 10 5 10-5M2 17l10 5 10-5"/></svg></div>
  <h3>Schilder &amp; Mehr</h3>
  <ul><li>Tür- &amp; Firmenschilder</li><li>Pokale &amp; Ehrenpreise</li><li>Zinn- &amp; Glasgravuren</li></ul>
</section>

<div class="abs about"></div>
<h2 class="abs sec-title about-title">Tradition trifft auf Innovation</h2>
<div class="abs about-text">
  <p>Als eingetragener <strong>Meisterbetrieb</strong> verbinden wir jahrzehntelange Erfahrung im klassischen Handwerk mit modernsten Technologien. Unsere Liebe zum Detail ist das Fundament unserer Arbeit.</p>
  <p>Wir beraten Sie persönlich und setzen Ihre Visionen millimetergenau um – ob für Industrie, Vereine oder ganz private Anlässe. Bei uns entstehen bleibende Werte.</p>
</div>
<div class="abs cert">
  <div class="cert-icon"><svg class="ic" viewBox="0 0 24 24"><path d="M7.2 15 2.7 7.7A2 2 0 0 1 2.5 6l1.4-2.9A2 2 0 0 1 5.7 2h12.6a2 2 0 0 1 1.8 1.1L21.5 6a2 2 0 0 1-.1 1.9L16.8 15"/><path d="M11 12 5.1 2.2M13 12l5.9-9.8M8 7h8"/><circle cx="12" cy="17" r="5"/></svg></div>
  <div><b>Meisterbrief</b><small>GEPRÜFTE QUALITÄT</small></div>
</div>
<div class="abs about-photo" role="img" aria-label="Foto: Hände bearbeiten Holz mit einem Stechbeitel, Späne auf der Werkbank"></div>

<div class="abs contact"></div>
<h2 class="abs sec-title contact-title">Sprechen wir über<br>Ihr Projekt</h2>
<div class="abs info" style="top:2162px">
  <div class="info-icon"><svg class="ic" viewBox="0 0 24 24"><path d="M20 10c0 6-8 12-8 12S4 16 4 10a8 8 0 0 1 16 0z"/><circle cx="12" cy="10" r="3"/></svg></div>
  <div><small>STANDORT</small><span>Musterstraße 123, 12345 Musterstadt</span></div>
</div>
<div class="abs info" style="top:2236px">
  <div class="info-icon"><svg class="ic" viewBox="0 0 24 24"><path d="M22 16.9v3a2 2 0 0 1-2.2 2 19.8 19.8 0 0 1-8.6-3.1 19.5 19.5 0 0 1-6-6A19.8 19.8 0 0 1 2.1 4.2 2 2 0 0 1 4.1 2h3a2 2 0 0 1 2 1.7c.1 1 .4 1.9.7 2.8a2 2 0 0 1-.5 2.1L8 9.9a16 16 0 0 0 6 6l1.3-1.3a2 2 0 0 1 2.1-.4c.9.3 1.8.6 2.8.7a2 2 0 0 1 1.7 2z"/></svg></div>
  <div><small>TELEFON</small><span>0123 456 789</span></div>
</div>
<div class="abs info" style="top:2310px">
  <div class="info-icon"><svg class="ic" viewBox="0 0 24 24"><rect x="2" y="4" width="20" height="16" rx="2"/><path d="m22 7-10 6L2 7"/></svg></div>
  <div><small>E-MAIL</small><span>info@gravierwerkstatt-brenner.de</span></div>
</div>
<aside class="abs hours">
  <h3>Öffnungszeiten</h3>
  <div class="row"><span>Mo. - Do.</span><b>08:00 - 17:00 Uhr</b></div>
  <div class="row"><span>Freitag</span><b>08:00 - 14:00 Uhr</b></div>
  <div class="row"><span>Sa. &amp; So.</span><em>Geschlossen</em></div>
  <div class="note"><svg class="ic" viewBox="0 0 24 24"><circle cx="12" cy="12" r="10"/><path d="M12 16v-4M12 8h.01"/></svg><span>Für persönliche Beratungsgespräche bitten wir Sie um eine vorherige Terminvereinbarung.</span></div>
</aside>

<footer>
  <div class="abs footer-rule"></div>
  <div class="abs footer-copy">© 2023 Gravierwerkstatt Brenner. Alle Rechte vorbehalten.</div>
  <div class="abs footer-links"><span>Impressum</span><span>Datenschutz</span><span>Barrierefreiheit</span></div>
</footer>

</body>
</html>
```